Lorvika.no is a new website about pedagogical entrepreneurship. It's main target group is teachers. The Fjellmark Institute for Classroom Media and the Nordvik Agency for Schools and Study are leading the project.

The web page is meant to show examples of how different methods of entrepreneurship can be used pedagogical in a learning environment. The page will also support the user with examples of different teaching programs and other examples of best practice.

Pedagogical entrepreneurship is not about business and men in suits. It's a method for learning. The focus in the design should be on school, education and new ways of learning.

The final product should be motivating and engaging, but at the same time governmental and serious. We are not looking for something "flashy" and corporate-looking, but a moderate, task-focused and clean design that state quality.

We need designs for three pages:
1 - frontpage
2 - subpage ("Metoder og undervisningsopplegg")
3 - subpage ("Smått-VERK i Brekkelia")

The interaction design for these three pages will be uploaded as an attachment.

We would like you to find inspiration in the following websites:
- www.gryvekst.no
- www.lavrek.no
- www.tovandstudio.com
- www.kvp.no
(more will be added)

Please use the attached logo, and feel free to use this as an inspiration for the rest of the design.

Target Market(s)

Teachers

Industry/Entity Type

Education

Requirements
Must have
• * Header with: Logo. Main navigation. Utility navigation. Search box.
* Footer
Should not have
• Images of men in suits.
Very strong graphical elements that stands out too much (we want it clean).

```html
<!DOCTYPE html>
<html lang="en">
<head>
<meta charset="utf-8">
<title>Lorvika.no – Pedagogical entrepreneurship</title>
<link rel="stylesheet" href="https://fonts.googleapis.com/css2?family=Signika:wght@300;400;600&family=Arimo:wght@400;700&display=swap">
<style>
:root{
  --navy:#1b4f85;
  --deep:#174a80;
  --blue:#2a6eb0;
  --sky:#38a6dc;
  --cyan:#2ab3d6;
  --text:#1d5a92;
  --ink:#111;
  --white:#fff;
  --footer:#1a4e85;
}
*{box-sizing:border-box;margin:0;padding:0}
html,body{width:1121px;height:1200px;overflow:hidden;background:var(--footer)}
.page{position:absolute;left:0;top:0;width:1280px;height:1370px;transform:scale(.87578);transform-origin:0 0;overflow:hidden;font-family:Arimo,Arial,sans-serif;
  background:linear-gradient(180deg,#fff 0,#fff 170px,#e4f1f9 300px,#c9e3f3 440px,#cde5f4 900px,#9fcdeb 990px,#5aa3d6 1022px,var(--footer) 1027px,var(--footer) 100%)}
.page>*{position:absolute}
a{text-decoration:none;color:inherit}
.topline{left:0;top:0;width:1280px;height:10px;background:linear-gradient(90deg,#1b4f85,#5fb0df 40%,#1b4f85)}
.utility{top:17px;left:598px;display:flex;gap:26px;font-size:12.5px;font-weight:700;color:var(--deep)}
.utility .current{color:var(--cyan)}
.search{left:960px;top:10px;width:160px;height:30px;background:var(--blue);border-radius:0 0 4px 4px;color:#9cc3e6;font-size:12px;padding:8px 12px}
.search svg{position:absolute;right:10px;top:5px}
.brand{left:150px;top:48px;display:flex;align-items:center;gap:14px;font-family:Signika,sans-serif;font-weight:600;font-size:54px;color:var(--blue);letter-spacing:-1px}
.brand i{width:62px;height:62px;border-radius:50%;background:var(--blue);display:block}
.hero{left:630px;top:96px;font-family:Signika,sans-serif;color:var(--text)}
.hero h1{font-weight:300;font-size:43px;letter-spacing:.3px}
.hero p{font-weight:600;font-size:19.5px;margin-top:6px;letter-spacing:.2px}
.hero .flourish{width:195px;height:26px;margin:8px 0 0 108px;border-radius:50%;background:radial-gradient(ellipse,rgba(27,79,133,.35),rgba(27,79,133,0) 70%)}
.feature{top:238px;width:300px;height:130px;font-family:Signika,sans-serif}
.feature h2{position:absolute;font-weight:300;font-size:26px;line-height:30px;color:var(--text)}
.feature .icon{position:absolute;left:4px;width:80px;height:84px;border-radius:12px;background:linear-gradient(160deg,#5fbbe9,#2a6eb0);opacity:.85}
.btn{position:absolute;height:22px;background:linear-gradient(180deg,#5fbbe9,#2d8fcb);color:#fff;font-family:Signika,sans-serif;font-weight:600;font-size:13.5px;padding:3px 10px;border-radius:2px;white-space:nowrap}
.btn .go{position:absolute;right:-14px;top:-5px;width:32px;height:32px}
.divider{top:255px;width:0;height:110px;border-left:1px dashed #8ebfe3}
.shade{height:16px;border-radius:50%;background:radial-gradient(ellipse,rgba(80,100,120,.35),transparent 70%)}
.panel{background:linear-gradient(100deg,#fff 55%,#e6e6e6);border-radius:4px;box-shadow:0 2px 3px rgba(0,0,0,.15)}
.panel>header{height:33px;background:linear-gradient(180deg,#3b7fc0,#1f5a95);border-radius:4px 4px 0 0;color:#fff;font-family:Signika,sans-serif;font-weight:300;font-size:22px;padding:3px 13px}
.quiz .icon{position:absolute;left:20px;top:64px;width:96px;height:96px;border-radius:14px;background:linear-gradient(160deg,#7cc8ee,#2a8fd0);opacity:.8}
.quiz h3{position:absolute;left:130px;top:54px;font-family:Signika,sans-serif;font-weight:600;font-size:23px;line-height:25px;color:var(--blue)}
.quiz p{position:absolute;left:130px;top:108px;font-family:Signika,sans-serif;font-weight:300;font-size:15px;line-height:18px;color:var(--blue)}
.col{position:absolute;top:40px}
.col h3{font-family:Signika,sans-serif;font-weight:600;font-size:25px;color:var(--deep);margin-bottom:4px}
.col li{list-style:none;font-size:16px;line-height:24px;color:var(--blue)}
.story{position:absolute;top:42px;width:300px}
.photo{position:absolute;left:0;top:4px;width:146px;height:146px;box-shadow:0 2px 4px rgba(0,0,0,.3)}
.story .txt{position:absolute;left:156px;top:0;width:136px;color:var(--ink)}
.story h4{font-weight:400;font-size:16px;line-height:20px}
.story p{font-size:12px;line-height:14.5px;margin-top:10px}
.story .more{display:block;font-size:12.5px;margin-top:8px}
.arrow{width:20px;height:52px;background:linear-gradient(180deg,#2d7fc0,#1b5a99);color:#fff;font-weight:700;text-align:center;line-height:52px;font-size:18px}
.dots{left:598px;top:914px;display:flex;gap:7px}
.dots i{width:16px;height:16px;border-radius:50%;border:2px solid var(--blue);background:#fff}
.dots i.on{background:var(--sky)}
.foot-rule{left:0;top:1114px;width:1280px;height:1px;background:#3f86c6}
.foot-brand{left:172px;top:1058px;display:flex;align-items:center;gap:12px;font-family:Signika,sans-serif;font-weight:600;font-size:40px;color:#bfe3f7}
.foot-brand i{width:44px;height:44px;border-radius:50%;background:#bfe3f7;display:block}
.foot-head{top:1058px;display:flex;align-items:center;gap:8px;font-family:Signika,sans-serif;font-weight:400;font-size:21px;line-height:24px;color:#fff}
.foot-head .icon{width:40px;height:44px;border-radius:8px;background:rgba(255,255,255,.85);display:block}
.foot-list{top:1124px;list-style:none;font-size:12.5px;line-height:24px;color:#dbe9f5}
.foot-list li::before{content:"» ";font-size:10px}
.foot-list .current{color:#45d0f0}
.copy{left:181px;top:1124px;font-size:12.5px;color:#6fc0ec}
</style>
</head>
<body>
<div class="page">
  <div class="topline"></div>
  <nav class="utility">
    <a class="current" href="#">Best practice schools</a>
    <a href="#">Lorvimeter</a>
    <a href="#">About lorvika.no</a>
  </nav>
  <div class="search">Searching for...
    <svg width="22" height="20" viewBox="0 0 22 20"><circle cx="8" cy="8" r="5.5" fill="none" stroke="#b9d6ef" stroke-width="2"/><path d="M12 12l7 6" stroke="#b9d6ef" stroke-width="3"/></svg>
  </div>

  <a class="brand" href="#"><i></i>Lorvika</a>

  <section class="hero">
    <h1>Learning in new ways?</h1>
    <p>PEDAGOGICAL ENTREPRENEURSHIP WORKS!</p>
    <div class="flourish" role="img" aria-label="Decorative wave flourish"></div>
  </section>

  <article class="feature" style="left:170px">
    <div class="icon" role="img" aria-label="Magnifier and person illustration" style="top:6px"></div>
    <h2 style="left:90px;top:0">What is<br>pedagogical<br>entrepreneurship?</h2>
    <a class="btn" href="#" style="left:10px;top:97px;width:262px">LEARN ABOUT WHAT, WHY AND HOW!
      <svg class="go" viewBox="0 0 32 32"><rect x="5" y="5" width="22" height="22" transform="rotate(45 16 16)" fill="#fff"/><rect x="8" y="8" width="16" height="16" transform="rotate(45 16 16)" fill="#1b4f85"/><path d="M14 11l5 5-5 5" stroke="#fff" stroke-width="3" fill="none"/></svg></a>
  </article>
  <div class="divider" style="left:482px"></div>
  <article class="feature" style="left:504px">
    <div class="icon" role="img" aria-label="Methods illustration" style="top:4px"></div>
    <h2 style="left:90px;top:30px">Methods and<br>teaching plans</h2>
    <a class="btn" href="#" style="left:0;top:97px;width:264px">PLAIN YOUR LESSONS!
      <svg class="go" viewBox="0 0 32 32"><rect x="5" y="5" width="22" height="22" transform="rotate(45 16 16)" fill="#fff"/><rect x="8" y="8" width="16" height="16" transform="rotate(45 16 16)" fill="#1b4f85"/><path d="M14 11l5 5-5 5" stroke="#fff" stroke-width="3" fill="none"/></svg></a>
  </article>
  <div class="divider" style="left:806px"></div>
  <article class="feature" style="left:829px">
    <div class="icon" role="img" aria-label="Sprouting plant illustration" style="top:4px"></div>
    <h2 style="left:90px;top:30px">Good examples,<br>best practice</h2>
    <a class="btn" href="#" style="left:0;top:97px;width:266px">BE INSPIRED!
      <svg class="go" viewBox="0 0 32 32"><rect x="5" y="5" width="22" height="22" transform="rotate(45 16 16)" fill="#fff"/><rect x="8" y="8" width="16" height="16" transform="rotate(45 16 16)" fill="#1b4f85"/><path d="M14 11l5 5-5 5" stroke="#fff" stroke-width="3" fill="none"/></svg></a>
  </article>
  <div class="shade" style="left:190px;top:394px;width:240px"></div>
  <div class="shade" style="left:512px;top:394px;width:245px"></div>
  <div class="shade" style="left:838px;top:394px;width:245px"></div>

  <div class="shade" style="left:180px;top:672px;width:280px"></div>
  <section class="panel quiz" style="left:170px;top:468px;width:300px;height:205px">
    <header>Test youself!</header>
    <div class="icon" role="img" aria-label="Gauge illustration"></div>
    <h3>Try the<br>lorvimeter!</h3>
    <p>Are you working<br>entrepreneurship like?</p>
    <a class="btn" href="#" style="left:130px;top:152px;width:140px">START QUIZ
      <svg class="go" viewBox="0 0 32 32"><rect x="5" y="5" width="22" height="22" transform="rotate(45 16 16)" fill="#fff"/><rect x="8" y="8" width="16" height="16" transform="rotate(45 16 16)" fill="#1b4f85"/><path d="M14 11l5 5-5 5" stroke="#fff" stroke-width="3" fill="none"/></svg></a>
  </section>

  <div class="shade" style="left:505px;top:672px;width:605px"></div>
  <section class="panel" style="left:495px;top:468px;width:625px;height:205px">
    <header>Get started!</header>
    <div class="col" style="left:20px">
      <h3>Teaching plans</h3>
      <ul><li>» Lorem ipsum dolor sit amet</li><li>» Onsectetur adipiscing elit</li><li>» Onsectetur</li><li>» Adipiscing elit dolor sit</li><li>» Dolor sit lorem ipsum.</li></ul>
    </div>
    <div style="position:absolute;left:311px;top:46px;height:146px;border-left:1px solid #bcd3e6"></div>
    <div class="col" style="left:340px">
      <h3>Methods</h3>
      <ul><li>» Café-pedagogikk</li><li>» Elevbedrift</li><li>» Gründercamp</li><li>» Story line</li><li>» Real</li></ul>
    </div>
  </section>

  <div class="shade" style="left:185px;top:942px;width:915px;height:20px"></div>
  <section class="panel" style="left:170px;top:698px;width:950px;height:245px">
    <header>Get Inspired!</header>
    <article class="story" style="left:23px">
      <div class="photo" role="img" aria-label="Photo of a student holding a stack of books in a library" style="background:linear-gradient(135deg,#f1d39a,#e7b36a 50%,#c7d9e8)"></div>
      <div class="txt"><h4>Lorem ipsum dolor sit amet</h4><p>Onsectetur adipiscing elit. Onsectetur elit dolor onsectetur adipiscing elit, sectetur adipiscing dolor elit</p><a class="more" href="#">» Read more</a></div>
    </article>
    <article class="story" style="left:339px">
      <div class="photo" role="img" aria-label="Photo of pupils writing at their desks in a classroom" style="background:linear-gradient(135deg,#7a5a48,#c9a58a 55%,#ece4dc)"></div>
      <div class="txt"><h4>Lorem ipsum dolor sit amet</h4><p>Onsectetur adipiscing elit. Onsectetur elit dolor onsectetur adipiscing elit, sectetur adipiscing dolor elit</p><a class="more" href="#">» Read more</a></div>
    </article>
    <article class="story" style="left:651px">
      <div class="photo" role="img" aria-label="Photo of a student concentrating on her work at a desk" style="background:linear-gradient(135deg,#f2eeea,#a87a5c 60%,#ddd)"></div>
      <div class="txt"><h4>Lorem ipsum dolor sit amet</h4><p>Onsectetur adipiscing elit. Onsectetur elit dolor onsectetur adipiscing elit, sectetur adipiscing dolor elit</p><a class="more" href="#">» Read more</a></div>
    </article>
  </section>
  <a class="arrow" href="#" style="left:150px;top:800px">‹</a>
  <a class="arrow" href="#" style="left:1120px;top:800px;background:linear-gradient(180deg,#3ad0ee,#1aa6cf)">›</a>
  <div class="dots"><i></i><i class="on"></i><i></i><i></i></div>

  <a class="foot-brand" href="#"><i></i>Lorvika</a>
  <div class="foot-head" style="left:440px">
    <i class="icon" role="img" aria-label="Magnifier and person illustration"></i>
    <span>Pedagogical<br>entrepreneurship</span></div>
  <div class="foot-head" style="left:746px">
    <i class="icon" role="img" aria-label="Methods illustration"></i>
    <span>Methods</span></div>
  <div class="foot-head" style="left:946px">
    <i class="icon" role="img" aria-label="Sprouting plant illustration"></i>
    <span>Inspirations</span></div>
  <div class="foot-rule"></div>
  <p class="copy">All rights reserved | Lorvika.no 2012</p>
  <ul class="foot-list" style="left:489px"><li>What is Pedagogical entrepreneurship?</li><li>Science</li><li>Best practice schools</li><li>Lorvimeter</li><li>About lorvika.no</li></ul>
  <ul class="foot-list" style="left:793px"><li class="current">Story line</li><li>Real</li><li>Café-pedagogikk</li><li>Blabla</li></ul>
  <ul class="foot-list" style="left:989px"><li>Lorem ipsum</li><li>Dolor sit amet</li><li>Onsectetur</li><li>Adipiscing elit</li></ul>
</div>
</body>
</html>
```